Fire Risk Assessment App needs a sleek UI design

I need a sleek, modern but professional design for my 5 page Fire Risk Assessment App. Include gradient background, fire themed colours including reds, yellows, light orange and a touch of black. Design must ooze simplicity and professionalism. This is for the UK market. See attached images and word doc for more information.

Target Market(s)

General public and business owners

Industry/Entity Type

Technology / Fire Safety

Colors
00AB8E
00BBA5
67D7C9
C6EFE9
E9F9F6
59FF00
82FF00
B8FF75
E3FFCB
F4FFEA
FFC000
F8CF3A
FAE287
FDF2CF
FEFAEE
F0912C
F2A743
F7CA91
FBE8D2
FDF5EE
EE7325
F08F49
F5BC92
FAE3D3
FDF4ED
EB3D1F
EC4F4E
F09395
F8D3D4
FCEDEE

```html
<!DOCTYPE html>
<html lang="en">
<head>
<meta charset="utf-8">
<title>Fire Risk Assessment App – Screens</title>
<link href="https://fonts.googleapis.com/css2?family=Outfit:wght@400;500;600;700&display=swap" rel="stylesheet">
<style>
  :root{
    --bg:#F3EEE8;
    --ink:#1c1c1c;
    --muted:#6b6b6b;
    --red:#EB3D1F;
    --rose:#EC4F4E;
    --coral:#E8603F;
    --orange:#F0912C;
    --amber:#FFC000;
    --cream:#FEFAEE;
    --peach:#FBE8D2;
    --sand:#F7CA91;
    --line:#F09395;
    --white:#ffffff;
  }
  *{box-sizing:border-box;margin:0;padding:0}
  html,body{width:1200px;height:1200px;overflow:hidden}
  body{background:var(--bg);font-family:"Outfit",sans-serif;color:var(--ink);position:relative}
  .screen{position:absolute;width:262px;height:568px;border-radius:28px;overflow:hidden;background:var(--white);box-shadow:0 6px 18px rgba(120,60,20,.08)}
  .screen *{position:absolute}
  .hero{left:0;top:0;width:100%;height:110px;background:
      radial-gradient(ellipse 60% 70% at 30% 70%,#F0621E 0%,rgba(200,40,10,.6) 40%,transparent 75%),
      radial-gradient(ellipse 50% 60% at 80% 40%,#E8461A 0%,rgba(150,20,5,.5) 45%,transparent 80%),
      linear-gradient(180deg,#1a0a06 0%,#3b0d05 55%,#7a1a08 100%)}
  .hero.tall{height:250px;background:
      radial-gradient(ellipse 40% 70% at 50% 65%,#FDF2CF 0%,#f5e2cf 60%,transparent 61%),
      linear-gradient(180deg,#3b0d05 0%,#8a2a10 35%,#dcd6d2 36%,#e6e2de 100%)}
  .panel{left:0;top:90px;width:100%;bottom:0;background:var(--white);border-radius:22px 22px 0 0;box-shadow:0 -4px 14px rgba(0,0,0,.08)}
  .panel.warm{top:66px;background:linear-gradient(180deg,var(--cream) 0%,#FDEBD0 45%,var(--sand) 100%)}
  .pill{left:21px;top:44px;height:22px;padding:0 8px 0 24px;background:var(--red);border-radius:6px 6px 0 0;color:var(--white);font-size:15.5px;font-weight:500;line-height:22px;white-space:nowrap;position:absolute}
  .pill svg{left:6px;top:4px;width:14px;height:14px}
  .title{font-size:17.5px;font-weight:400;white-space:nowrap}
  .sub{font-size:10px;white-space:nowrap}
  .label{font-size:10px;left:25px;white-space:nowrap}
  .input{left:25px;width:219px;height:33px;border:1px solid var(--line);border-radius:6px;background:var(--white)}
  .btn{height:33px;border-radius:6px;background:linear-gradient(90deg,#F2210E 0%,#F5581A 50%,#F7941F 100%);color:var(--white);font-size:10px;text-align:center;line-height:33px;box-shadow:0 4px 10px rgba(235,61,31,.25)}
  .btn.big{font-size:12.5px;font-weight:600;height:41px;line-height:41px}
  .link{color:var(--red);text-decoration:underline}
  .terms{left:23px;width:225px;font-size:7.3px;line-height:14px}
  .section{font-size:12px;font-weight:600;color:var(--coral);white-space:nowrap}
  .hint{font-size:8.5px;white-space:nowrap}
  .tile{width:113px;height:76px;background:var(--white);border-radius:6px;box-shadow:0 2px 6px rgba(0,0,0,.05)}
  .tile .num{left:7px;top:2px;font-size:18px;font-weight:600}
  .tile .cap{left:7px;top:26px;font-size:9px;line-height:12px;width:100px}
  .tile .go{left:7px;top:58px;font-size:9px;color:var(--coral);width:98px}
  .tile .go svg{right:0;top:2px;width:12px;height:9px}
  .nav{left:6px;top:517px;width:250px;height:41px;background:var(--white);border-radius:8px;box-shadow:0 2px 8px rgba(0,0,0,.06)}
  .nav .ic{width:16px;height:16px;top:12px}
  .nav .hub{left:107px;top:2px;width:37px;height:37px;border-radius:50%;background:radial-gradient(circle,#f3f3f3 0%,#d8d8d8 70%,#bdbdbd 100%)}
  .nav .active{height:3px;width:20px;background:var(--red);top:38px;border-radius:2px}
  .field{left:18px;width:230px;height:38px;background:var(--white);border-radius:6px;box-shadow:0 2px 6px rgba(0,0,0,.05);font-size:11px;line-height:38px;padding-left:36px}
  .field svg{left:10px;top:10px;width:18px;height:18px}
  .package{left:15px;width:231px;height:34px;background:var(--white);border-radius:4px;box-shadow:0 2px 6px rgba(0,0,0,.05)}
  .package .medal{left:5px;top:4px;width:26px;height:26px;border-radius:50%}
  .package .name{left:37px;top:0;line-height:34px;font-size:10.5px;font-weight:500;white-space:nowrap}
  .package .price{right:12px;top:0;line-height:34px;font-size:15px;font-weight:500;white-space:nowrap}
  .package .price sup{position:static;font-size:8px}
  .tag{width:60px;height:13px;background:var(--rose);color:var(--white);font-size:7.5px;text-align:center;line-height:13px;border-radius:2px 2px 0 0;left:175px}
  .bubble{background:var(--white);border-radius:10px;font-size:9.5px;line-height:13px;padding:10px 10px}
  .avatar{width:19px;height:19px;font-size:9px;color:var(--white);text-align:center;line-height:19px;font-weight:500}
  .meta{font-size:6px;color:var(--muted)}
  .recent{left:14px;width:234px;height:40px;background:var(--white);border-radius:6px;box-shadow:0 2px 6px rgba(0,0,0,.05)}
  .recent svg{left:16px;top:5px;width:18px;height:18px}
  .recent .bn{left:42px;top:6px;font-size:11.5px;white-space:nowrap}
  .recent .dt{left:15px;top:25px;font-size:7.5px;color:var(--muted);white-space:nowrap}
</style>
</head>
<body>

<!-- Screen 1: create account -->
<section class="screen" style="left:38px;top:32px">
  <div class="hero" role="img" aria-label="Close-up photo of flames on a dark background"></div>
  <div class="panel">
    <h1 class="title" style="left:26px;top:26px">Welcome</h1>
    <svg style="left:25px;top:56px;width:14px;height:14px" viewBox="0 0 14 14"><rect width="14" height="14" rx="3" fill="#FCEDEE"/><circle cx="6" cy="5" r="2.2" fill="none" stroke="#EC4F4E"/><path d="M2.5 11c.6-2.2 2-3 3.5-3s2.3.5 3 1.4M10 9v3M8.5 10.5h3" fill="none" stroke="#EC4F4E"/></svg>
    <p class="sub" style="left:46px;top:57px">Kindly create an account below</p>
    <p class="label" style="top:89px">Username</p>
    <div class="input" style="top:108px"></div>
    <p class="label" style="top:145px">Password</p>
    <div class="input" style="top:163px"></div>
    <p class="label" style="top:200px">Full name</p>
    <div class="input" style="top:218px"></div>
    <p class="label" style="top:256px">Business name</p>
    <div class="input" style="top:274px"></div>
    <div class="btn" style="left:25px;top:334px;width:216px">Create account</div>
    <p class="sub" style="left:25px;top:377px">An existing client? <span class="link" style="position:static">Login instead</span></p>
    <p class="terms" style="top:403px">Welcome to 'Fire Risk Assessment'! By clicking signing up, you agree to the following terms and conditions.</p>
  </div>
</section>

<!-- Screen 2: fingerprint registration -->
<section class="screen" style="left:330px;top:32px">
  <div class="hero" role="img" aria-label="Close-up photo of flames on a dark background"></div>
  <div class="panel">
    <svg style="left:114px;top:23px;width:34px;height:30px" viewBox="0 0 34 30"><rect width="34" height="30" rx="5" fill="#FCEDEE"/><circle cx="15" cy="10" r="4" fill="none" stroke="#EC4F4E" stroke-width="1.3"/><path d="M8 23c1-4 4-6 7-6 2 0 3.5.6 4.5 1.5" fill="none" stroke="#EC4F4E" stroke-width="1.3"/><path d="M22 17l4 1.5v3c0 2-2 3.5-4 4-2-.5-4-2-4-4v-3z" fill="#EC4F4E"/></svg>
    <h1 class="title" style="left:0;width:262px;text-align:center;top:61px">Identity Protection</h1>
    <p class="sub" style="left:0;width:262px;text-align:center;top:86px;font-size:8.8px;line-height:14px;white-space:normal;padding:0 28px">To ensure all our client 's information and data are safe, we advise to provide finger print</p>
    <svg style="left:89px;top:154px;width:76px;height:76px" viewBox="0 0 76 76" fill="none" stroke="#EB3D1F" stroke-width="2.2" stroke-linecap="round">
      <circle cx="38" cy="38" r="37" stroke-width="1.2" stroke="#EC4F4E"/>
      <path d="M22 30a17 17 0 0 1 32 0"/><path d="M17 42a21 21 0 0 1 4-17"/><path d="M26 52c-3-5-3-12 1-17a13 13 0 0 1 22 4c1 5 0 10-2 14"/>
      <path d="M32 56c-3-5-4-11-1-16a8 8 0 0 1 14 2c1 5 0 10-3 15"/><path d="M38 58c-2-5-2-10-1-14"/><path d="M57 38c1 6 0 12-3 17"/>
    </svg>
    <p class="sub" style="left:0;width:262px;text-align:center;top:240px">Register your finger print</p>
    <div style="left:29px;top:264px;width:212px;height:3px;background:#eee;border-radius:2px"></div>
    <div style="left:29px;top:264px;width:118px;height:3px;background:linear-gradient(90deg,#EB3D1F,#F0912C);border-radius:2px"></div>
    <p class="sub" style="left:0;width:262px;text-align:center;top:276px;font-size:9px">55%</p>
    <div class="btn" style="left:25px;top:334px;width:216px">Sign in</div>
    <p class="sub" style="left:25px;top:377px">An existing client? <span class="link" style="position:static">Login instead</span></p>
    <p class="terms" style="top:403px">Welcome to 'Fire Risk Assessment'! By clicking signing up, you agree to the following terms and conditions.</p>
  </div>
</section>

<!-- Screen 3: sign in -->
<section class="screen" style="left:622px;top:32px">
  <div class="hero tall" role="img" aria-label="Phone showing the dashboard screen, over flames"></div>
  <div class="panel" style="top:232px">
    <h1 class="title" style="left:25px;top:22px">Welcome</h1>
    <svg style="left:25px;top:54px;width:14px;height:14px" viewBox="0 0 14 14"><rect width="14" height="14" rx="3" fill="#FCEDEE"/><circle cx="7" cy="5" r="2.2" fill="none" stroke="#EC4F4E"/><path d="M3 11.5c.6-2.2 2-3 4-3s3.4.8 4 3z" fill="none" stroke="#EC4F4E"/></svg>
    <p class="sub" style="left:50px;top:55px">Kindly sign in below</p>
    <p class="label" style="top:83px">Username</p>
    <div class="input" style="top:100px;width:218px"></div>
    <p class="label" style="top:141px">Password</p>
    <div class="input" style="top:158px;width:218px"></div>
    <p class="sub" style="left:25px;top:200px">Forget password? <span class="link" style="position:static">Retrieve here</span></p>
    <div class="btn" style="left:25px;top:235px;width:173px">Sign in</div>
    <div style="left:206px;top:235px;width:37px;height:33px;border-radius:6px;background:#FCEDEE;border:1px solid var(--line)">
      <svg style="left:8px;top:6px;width:20px;height:20px" viewBox="0 0 76 76" fill="none" stroke="#EB3D1F" stroke-width="4" stroke-linecap="round"><path d="M22 30a17 17 0 0 1 32 0"/><path d="M26 52c-3-5-3-12 1-17a13 13 0 0 1 22 4c1 5 0 10-2 14"/><path d="M32 56c-3-5-4-11-1-16a8 8 0 0 1 14 2c1 5 0 10-3 15"/><path d="M57 38c1 6 0 12-3 17"/></svg>
    </div>
    <p class="sub" style="left:25px;top:276px">Don't have an account? <span class="link" style="position:static">Sign up instead</span></p>
  </div>
</section>

<!-- Screen 4: dashboard empty -->
<section class="screen" style="left:914px;top:32px">
  <div class="hero" role="img" aria-label="Close-up photo of flames on a dark background"></div>
  <div class="pill"><svg viewBox="0 0 14 14" fill="none" stroke="#fff" stroke-width="1.4"><circle cx="7" cy="7" r="6"/><path d="M7 7l3-3"/></svg>Dashboard</div>
  <div class="panel warm">
    <svg style="left:22px;top:16px;width:17px;height:17px" viewBox="0 0 17 17"><circle cx="8.5" cy="8.5" r="8" fill="#1c1c1c"/><circle cx="8.5" cy="6.5" r="3" fill="#fff"/><path d="M3 14c1.5-3 3.5-4 5.5-4s4 1 5.5 4" fill="#fff"/></svg>
    <p style="left:47px;top:15px;font-size:12.5px;white-space:nowrap">Hello <b style="position:static;font-weight:600">Darren</b></p>
    <svg style="left:236px;top:17px;width:13px;height:15px" viewBox="0 0 13 15"><path d="M6.5 1a4 4 0 0 1 4 4v4l2 2.5H0.5L2.5 9V5a4 4 0 0 1 4-4z" fill="#1c1c1c"/><circle cx="6.5" cy="13.5" r="1.5" fill="#1c1c1c"/></svg>
    <div class="btn big" style="left:20px;top:50px;width:225px"><span style="position:static">⊕</span> Start Fire Risk Assessment</div>
    <p class="section" style="left:21px;top:108px">Assessment Overview</p>
    <p class="hint" style="right:12px;top:110px">View all</p>
    <div class="tile" style="left:14px;top:134px"><p class="num">0</p><p class="cap">Completed Fire Risk Assessments</p><p class="go">View all<svg viewBox="0 0 12 9" fill="none" stroke="#E8603F" stroke-width="1.2"><path d="M0 4.5h11M7.5 1l3.5 3.5L7.5 8"/></svg></p></div>
    <div class="tile" style="left:135px;top:134px"><p class="num">0</p><p class="cap">In progress Fire Risk Assessments</p><p class="go">Continue<svg viewBox="0 0 12 9" fill="none" stroke="#E8603F" stroke-width="1.2"><path d="M0 4.5h11M7.5 1l3.5 3.5L7.5 8"/></svg></p></div>
    <div class="tile" style="left:14px;top:216px"><p class="num">0</p><p class="cap">Purchased Fire Risk Assessments</p><p class="go">View all<svg viewBox="0 0 12 9" fill="none" stroke="#E8603F" stroke-width="1.2"><path d="M0 4.5h11M7.5 1l3.5 3.5L7.5 8"/></svg></p></div>
    <div class="tile" style="left:135px;top:216px"><p class="num">0</p><p class="cap">In progress Fire Risk Assessments</p></div>
    <p class="section" style="left:21px;top:325px">Recent Created Assessment</p>
    <p style="left:21px;top:341px;font-size:7.5px;white-space:nowrap">You have no recent assessment created</p>
    <div role="img" aria-label="Illustration of empty assessment documents" style="left:70px;top:362px;width:104px;height:76px;border-radius:4px;background:linear-gradient(135deg,#ffffff 0%,#FDF4ED 60%,#FBE8D2 100%)"></div>
  </div>
  <div class="nav">
    <svg class="ic" style="left:18px" viewBox="0 0 16 16" fill="none" stroke="#EB3D1F" stroke-width="1.5"><circle cx="8" cy="8" r="7"/><path d="M8 8l3-3"/></svg>
    <svg class="ic" style="left:62px" viewBox="0 0 16 16" fill="none" stroke="#aaa" stroke-width="1.3"><rect x="1" y="3" width="14" height="10" rx="2"/><path d="M1 7h14"/></svg>
    <div class="hub" role="img" aria-label="App emblem"></div>
    <svg class="ic" style="left:172px" viewBox="0 0 16 16" fill="none" stroke="#aaa" stroke-width="1.3"><path d="M3 8a5 5 0 0 1 10 0v3"/><rect x="2" y="8" width="3" height="4" rx="1"/><path d="M8 15h4"/></svg>
    <svg class="ic" style="left:216px" viewBox="0 0 16 16" fill="none" stroke="#aaa" stroke-width="1.3"><path d="M2 14l7-7M9 7a3 3 0 1 0 3-4l-2 2 1 1 2-2"/></svg>
    <div class="active" style="left:16px"></div>
  </div>
</section>

<!-- Screen 5: payment options -->
<section class="screen" style="left:38px;top:618px">
  <div class="hero" role="img" aria-label="Close-up photo of flames on a dark background"></div>
  <div class="pill"><svg viewBox="0 0 14 14" fill="none" stroke="#fff" stroke-width="1.4"><rect x="1" y="3" width="12" height="9" rx="2"/><path d="M1 6.5h12"/></svg>Payment Options</div>
  <div class="panel warm">
    <p class="section" style="left:15px;top:20px">Purchase Fire Risk Assessment</p>
    <p style="left:15px;top:35px;font-size:9.5px;white-space:nowrap">Select preferred payment option</p>
    <div class="package" style="top:64px"><div class="medal" style="background:#8a2418"></div><p class="name">Bronze Package(1):</p><p class="price">£19.<sup>99</sup></p></div>
    <div class="tag" style="top:111px">Savings Option</div>
    <div class="package" style="top:124px"><div class="medal" style="background:#b5b5b5"></div><p class="name">Silver Package(3):</p><p class="price">£54.<sup>99</sup></p></div>
    <div class="tag" style="top:173px">Savings Option</div>
    <div class="package" style="top:186px"><div class="medal" style="background:#E8B31A"></div><p class="name">Gold Package(5):</p><p class="price">£89.<sup>99</sup></p></div>
    <div class="tag" style="top:234px">Savings Option</div>
    <div class="package" style="top:247px"><div class="medal" style="background:#2f5da8"></div><p class="name">Platinum Package(10):</p><p class="price">£89.<sup>99</sup></p></div>
    <div class="btn big" style="left:18px;top:327px;width:225px">Proceed</div>
  </div>
  <div class="nav">
    <svg class="ic" style="left:18px" viewBox="0 0 16 16" fill="none" stroke="#aaa" stroke-width="1.3"><circle cx="8" cy="8" r="7"/><path d="M8 8l3-3"/></svg>
    <svg class="ic" style="left:62px" viewBox="0 0 16 16" fill="none" stroke="#EB3D1F" stroke-width="1.5"><rect x="1" y="3" width="14" height="10" rx="2"/><path d="M1 7h14"/></svg>
    <div class="hub" role="img" aria-label="App emblem"></div>
    <svg class="ic" style="left:172px" viewBox="0 0 16 16" fill="none" stroke="#aaa" stroke-width="1.3"><path d="M3 8a5 5 0 0 1 10 0v3"/><rect x="2" y="8" width="3" height="4" rx="1"/><path d="M8 15h4"/></svg>
    <svg class="ic" style="left:216px" viewBox="0 0 16 16" fill="none" stroke="#aaa" stroke-width="1.3"><path d="M2 14l7-7M9 7a3 3 0 1 0 3-4l-2 2 1 1 2-2"/></svg>
    <div class="active" style="left:60px"></div>
  </div>
</section>

<!-- Screen 6: customer support -->
<section class="screen" style="left:330px;top:618px">
  <div class="hero" role="img" aria-label="Close-up photo of flames on a dark background"></div>
  <div class="pill"><svg viewBox="0 0 14 14" fill="none" stroke="#fff" stroke-width="1.4"><path d="M2 8a5 5 0 0 1 10 0v2"/><rect x="1" y="7" width="3" height="4" rx="1"/><path d="M7 13h4"/></svg>Customer Support</div>
  <div class="panel warm">
    <p class="section" style="left:14px;top:20px">Technical support</p>
    <p style="left:14px;top:35px;font-size:9.5px;white-space:nowrap">Type /record your message</p>
    <div class="bubble" style="left:88px;top:136px;width:154px;height:64px">I want to purchase my risk assessment package cant get over it</div>
    <p class="meta" style="left:100px;top:190px">✓ Sent 3mins ago</p>
    <div class="avatar" style="left:224px;top:181px;background:var(--rose)">M</div>
    <div class="bubble" style="left:14px;top:218px;width:154px;height:51px;padding-left:26px">Hello Darren, how can we be of help to you?</div>
    <div class="avatar" style="left:14px;top:250px;background:var(--orange)">C</div>
    <div class="bubble" style="left:88px;top:280px;width:154px;height:56px">Hello i need help here concerning my form</div>
    <p class="meta" style="left:100px;top:322px;color:#2a9a5a">✓✓Read</p>
    <div class="avatar" style="left:224px;top:316px;background:var(--rose)">M</div>
    <div style="left:19px;top:374px;width:223px;height:40px;background:var(--white);border-radius:20px"></div>
    <p style="left:38px;top:388px;font-size:10px;color:#999;white-space:nowrap">Type here message</p>
    <svg style="left:201px;top:388px;width:18px;height:12px" viewBox="0 0 18 12" fill="none" stroke="#555" stroke-width="1"><rect x=".5" y=".5" width="17" height="11" rx="1.5"/><path d="M3 3.5h1M6 3.5h1M9 3.5h1M12 3.5h1M15 3.5h0M3 6h1M6 6h1M9 6h1M12 6h1M5 8.5h8"/></svg>
    <svg style="left:30px;top:423px;width:16px;height:14px" viewBox="0 0 16 14"><path d="M1 4h3l1.5-2h5L12 4h3v9H1z" fill="#555"/><circle cx="8" cy="8" r="2.8" fill="#fff"/></svg>
    <svg style="left:58px;top:420px;width:12px;height:18px" viewBox="0 0 12 18" fill="none" stroke="#555" stroke-width="1.4"><rect x="3" y="1" width="6" height="10" rx="3" fill="#555"/><path d="M1 8a5 5 0 0 0 10 0M6 13v4"/></svg>
  </div>
  <div class="nav">
    <svg class="ic" style="left:18px" viewBox="0 0 16 16" fill="none" stroke="#aaa" stroke-width="1.3"><circle cx="8" cy="8" r="7"/><path d="M8 8l3-3"/></svg>
    <svg class="ic" style="left:62px" viewBox="0 0 16 16" fill="none" stroke="#aaa" stroke-width="1.3"><rect x="1" y="3" width="14" height="10" rx="2"/><path d="M1 7h14"/></svg>
    <div class="hub" role="img" aria-label="App emblem"></div>
    <svg class="ic" style="left:172px" viewBox="0 0 16 16" fill="none" stroke="#EB3D1F" stroke-width="1.5"><path d="M3 8a5 5 0 0 1 10 0v3"/><rect x="2" y="8" width="3" height="4" rx="1"/><path d="M8 15h4"/></svg>
    <svg class="ic" style="left:216px" viewBox="0 0 16 16" fill="none" stroke="#aaa" stroke-width="1.3"><path d="M2 14l7-7M9 7a3 3 0 1 0 3-4l-2 2 1 1 2-2"/></svg>
    <div class="active" style="left:170px"></div>
  </div>
</section>

<!-- Screen 7: fire risk assessment progress -->
<section class="screen" style="left:622px;top:618px">
  <div class="hero" role="img" aria-label="Close-up photo of flames on a dark background"></div>
  <div class="pill"><svg viewBox="0 0 14 14"><path d="M7 1c1 3 4 4 4 8a4 4 0 0 1-8 0c0-2 1-3 2-4 0 2 1 2 1 2 0-3 1-4 1-6z" fill="#fff"/></svg>Fire Risk Assessment</div>
  <div class="panel warm">
    <p class="section" style="left:18px;top:20px">Building name:</p>
    <div class="field" style="top:42px"><svg viewBox="0 0 18 18"><path d="M9 2l8 7h-2v7H3V9H1z" fill="#F0912C"/><path d="M9 2l8 7H1z" fill="#EB3D1F"/><rect x="7" y="11" width="4" height="5" fill="#2f5da8"/></svg>CLAUSE 13 ANEX B</div>
    <p class="section" style="left:18px;top:95px">Fire Hazard</p>
    <div class="field" style="top:113px"><svg viewBox="0 0 18 18"><path d="M9 1c1.5 4 6 5 6 11a6 6 0 0 1-12 0c0-3 1.5-4.5 3-6 0 3 1.5 3 1.5 3 0-4 1.5-5 1.5-8z" fill="#EB3D1F"/></svg>Unknown/not provided</div>
    <p class="section" style="left:18px;top:168px">Assessment Progress</p>
    <div style="left:14px;top:196px;width:232px;height:76px;background:var(--white);border-radius:6px;box-shadow:0 2px 6px rgba(0,0,0,.05)"></div>
    <p style="left:25px;top:219px;font-size:9.5px;white-space:nowrap">Fire Risk Assessment</p>
    <p style="left:23px;top:234px;font-size:14px;white-space:nowrap">Section Progress</p>
    <svg style="left:166px;top:198px;width:70px;height:70px" viewBox="0 0 70 70" fill="none"><circle cx="35" cy="35" r="31" stroke="#e4e4e4" stroke-width="6"/><circle cx="35" cy="35" r="31" stroke="#EB3D1F" stroke-width="6" stroke-linecap="round" stroke-dasharray="30 200" transform="rotate(40 35 35)"/></svg>
    <p style="left:166px;top:220px;width:70px;text-align:center;font-size:22px;font-weight:600">15%</p>
    <div style="left:14px;top:284px;width:232px;height:84px;background:var(--white);border-radius:6px;box-shadow:0 2px 6px rgba(0,0,0,.05)"></div>
    <p style="left:20px;top:290px;font-size:9px;white-space:nowrap">Assessment Session:</p>
    <p style="right:24px;top:290px;font-size:9.5px;font-weight:600;white-space:nowrap">2.03 of 14.00</p>
    <div class="btn big" style="left:20px;top:319px;width:225px">Continue</div>
  </div>
  <div class="nav">
    <svg class="ic" style="left:18px" viewBox="0 0 16 16" fill="none" stroke="#aaa" stroke-width="1.3"><circle cx="8" cy="8" r="7"/><path d="M8 8l3-3"/></svg>
    <svg class="ic" style="left:62px" viewBox="0 0 16 16" fill="none" stroke="#aaa" stroke-width="1.3"><rect x="1" y="3" width="14" height="10" rx="2"/><path d="M1 7h14"/></svg>
    <div class="hub" role="img" aria-label="App emblem"></div>
    <svg class="ic" style="left:172px" viewBox="0 0 16 16" fill="none" stroke="#aaa" stroke-width="1.3"><path d="M3 8a5 5 0 0 1 10 0v3"/><rect x="2" y="8" width="3" height="4" rx="1"/><path d="M8 15h4"/></svg>
    <svg class="ic" style="left:216px" viewBox="0 0 16 16" fill="none" stroke="#aaa" stroke-width="1.3"><path d="M2 14l7-7M9 7a3 3 0 1 0 3-4l-2 2 1 1 2-2"/></svg>
  </div>
</section>

<!-- Screen 8: dashboard with data -->
<section class="screen" style="left:914px;top:618px">
  <div class="hero" role="img" aria-label="Close-up photo of flames on a dark background"></div>
  <div class="pill"><svg viewBox="0 0 14 14" fill="none" stroke="#fff" stroke-width="1.4"><circle cx="7" cy="7" r="6"/><path d="M7 7l3-3"/></svg>Dashboard</div>
  <div class="panel warm">
    <svg style="left:22px;top:16px;width:17px;height:17px" viewBox="0 0 17 17"><circle cx="8.5" cy="8.5" r="8" fill="#1c1c1c"/><circle cx="8.5" cy="6.5" r="3" fill="#fff"/><path d="M3 14c1.5-3 3.5-4 5.5-4s4 1 5.5 4" fill="#fff"/></svg>
    <p style="left:47px;top:15px;font-size:12.5px;white-space:nowrap">Hello <b style="position:static;font-weight:600">Darren</b></p>
    <svg style="left:236px;top:17px;width:13px;height:15px" viewBox="0 0 13 15"><path d="M6.5 1a4 4 0 0 1 4 4v4l2 2.5H0.5L2.5 9V5a4 4 0 0 1 4-4z" fill="#1c1c1c"/><circle cx="6.5" cy="13.5" r="1.5" fill="#1c1c1c"/></svg>
    <div class="btn big" style="left:20px;top:50px;width:225px"><span style="position:static">⊕</span> Start Fire Risk Assessment</div>
    <p class="section" style="left:21px;top:108px">Assessment Overview</p>
    <p class="hint" style="right:12px;top:110px">View all</p>
    <div class="tile" style="left:14px;top:134px"><p class="num">4</p><p class="cap">Completed Fire Risk Assessments</p><p class="go">View all<svg viewBox="0 0 12 9" fill="none" stroke="#E8603F" stroke-width="1.2"><path d="M0 4.5h11M7.5 1l3.5 3.5L7.5 8"/></svg></p></div>
    <div class="tile" style="left:135px;top:134px"><p class="num">1</p><p class="cap">In progress Fire Risk Assessments</p><p class="go">Continue<svg viewBox="0 0 12 9" fill="none" stroke="#E8603F" stroke-width="1.2"><path d="M0 4.5h11M7.5 1l3.5 3.5L7.5 8"/></svg></p></div>
    <div class="tile" style="left:14px;top:216px"><p class="num">4</p><p class="cap">Purchased Fire Risk Assessments</p><p class="go">View all<svg viewBox="0 0 12 9" fill="none" stroke="#E8603F" stroke-width="1.2"><path d="M0 4.5h11M7.5 1l3.5 3.5L7.5 8"/></svg></p></div>
    <div class="tile" style="left:135px;top:216px"><p class="num">0</p><p class="cap">In progress Fire Risk Assessments</p></div>
    <p class="section" style="left:14px;top:311px">Recent Created Assessment</p>
    <div class="recent" style="top:332px"><svg viewBox="0 0 18 18"><path d="M9 2l8 7h-2v7H3V9H1z" fill="#F0912C"/><path d="M9 2l8 7H1z" fill="#EB3D1F"/><rect x="7" y="11" width="4" height="5" fill="#2f5da8"/></svg><p class="bn">CLAUSE 13 ANEX B</p><p class="dt">Date created: 25-08-2024</p></div>
    <div class="recent" style="top:382px"><svg viewBox="0 0 18 18"><path d="M9 2l8 7h-2v7H3V9H1z" fill="#F0912C"/><path d="M9 2l8 7H1z" fill="#EB3D1F"/><rect x="7" y="11" width="4" height="5" fill="#2f5da8"/></svg><p class="bn">CLAUSE 13 ANEX B</p><p class="dt">Date created: 25-08-2024</p></div>
  </div>
  <div class="nav">
    <svg class="ic" style="left:18px" viewBox="0 0 16 16" fill="none" stroke="#EB3D1F" stroke-width="1.5"><circle cx="8" cy="8" r="7"/><path d="M8 8l3-3"/></svg>
    <svg class="ic" style="left:62px" viewBox="0 0 16 16" fill="none" stroke="#aaa" stroke-width="1.3"><rect x="1" y="3" width="14" height="10" rx="2"/><path d="M1 7h14"/></svg>
    <div class="hub" role="img" aria-label="App emblem"></div>
    <svg class="ic" style="left:172px" viewBox="0 0 16 16" fill="none" stroke="#aaa" stroke-width="1.3"><path d="M3 8a5 5 0 0 1 10 0v3"/><rect x="2" y="8" width="3" height="4" rx="1"/><path d="M8 15h4"/></svg>
    <svg class="ic" style="left:216px" viewBox="0 0 16 16" fill="none" stroke="#aaa" stroke-width="1.3"><path d="M2 14l7-7M9 7a3 3 0 1 0 3-4l-2 2 1 1 2-2"/></svg>
    <div class="active" style="left:16px"></div>
  </div>
</section>

</body>
</html>
```